Course Graduation Certificate

This project is not for a flyer but instead for the creation of a course graduation certificate. The final certificate needs to include the Marlowe Summit Aviation Academy logo and the text stating as follows:
Certifies that ___________________________ has satisfactorily completed the course of _______________________________ on ________________________________
I would also like to include some type of gold seal of completion as well as a place to sign my name and credentials at the bottom of the certificate
I have included the Marlowe Summit Aviation Academy logo as well as three other certificate examples for you to work from.
Target Market(s)
Students completing a certification course and receiving a certificate
Look and feel

```html
<!DOCTYPE html>
<html lang="en">
<head>
<meta charset="utf-8">
<title>Course Graduation Certificate</title>
<link rel="stylesheet" href="https://fonts.googleapis.com/css2?family=UnifrakturCook:wght@700&family=Great+Vibes&family=Open+Sans:wght@600;700&display=swap">
<style>
  :root {
    --page: #ffffff;
    --ink: #1b1b1b;
    --frame: #4a4a4a;
    --blue: #2468b4;
    --blue-deep: #1b4f8f;
    --dark-1: #1f1f20;
    --dark-2: #353536;
    --dark-3: #4b4b4d;
    --gold: #d7ad3e;
  }
  * { margin: 0; padding: 0; box-sizing: border-box; }
  html, body {
    width: 884px;
    height: 1200px;
    overflow: hidden;
    background: var(--page);
  }
  .canvas {
    position: relative;
    width: 884px;
    height: 1200px;
    display: flex;
    align-items: center;
    justify-content: center;
  }
  .certificate {
    display: block;
    width: 884px;
    height: 590px;
  }
  .title {
    font-family: "UnifrakturCook", "Times New Roman", serif;
    font-weight: 700;
    font-size: 122px;
    fill: var(--ink);
  }
  .label {
    font-family: "Open Sans", Arial, sans-serif;
    font-weight: 700;
    font-size: 32px;
    fill: var(--ink);
  }
  .signatory {
    font-family: "Open Sans", Arial, sans-serif;
    font-weight: 700;
    font-size: 21px;
    fill: var(--ink);
  }
  .recipient {
    font-family: "Great Vibes", cursive;
    font-size: 66px;
    fill: var(--ink);
  }
  .academy-name {
    font-family: "Open Sans", Arial, sans-serif;
    font-weight: 700;
    font-size: 25px;
    fill: var(--blue);
  }
  .rule { stroke: var(--blue); stroke-width: 2.5; }
  .rule-end { fill: var(--blue); }
  .dots { stroke: var(--blue-deep); stroke-width: 6; stroke-linecap: round; stroke-dasharray: 0 14; }
  .seal { fill: var(--gold); }
</style>
</head>
<body>
<main class="canvas">
  <svg class="certificate" viewBox="0 0 1597 1065" xmlns="http://www.w3.org/2000/svg" aria-labelledby="cert-title">
    <title id="cert-title">Certificate of Completion — Marlowe Summit Aviation Academy</title>
    <defs>
      <linearGradient id="paper-fade" x1="0" y1="0" x2="1" y2="1">
        <stop offset="0" stop-color="#ffffff"/>
        <stop offset="1" stop-color="#f2f3f5"/>
      </linearGradient>
    </defs>

    <g class="frames">
      <path d="M150,0 H1447 Q1450,80 1538,93 V1065 H58 V110 Q145,80 150,0 Z" fill="url(#paper-fade)" stroke="var(--frame)" stroke-width="1.2"/>
      <rect x="94" y="34" width="1408" height="1031" fill="none" stroke="var(--frame)" stroke-width="1.2"/>
    </g>

    <g class="sweep sweep-left">
      <path d="M0,685 Q230,960 520,1065 H0 Z" fill="var(--dark-1)"/>
      <path d="M0,760 Q210,975 430,1065 H0 Z" fill="var(--dark-2)"/>
      <path d="M0,850 Q180,1000 330,1065 H0 Z" fill="var(--dark-3)"/>
      <path d="M0,955 Q100,1020 180,1065 H0 Z" fill="var(--blue)"/>
    </g>
    <g class="sweep sweep-right">
      <path d="M1597,668 Q1450,950 1080,1065 H1597 Z" fill="var(--dark-1)"/>
      <path d="M1597,750 Q1480,975 1200,1065 H1597 Z" fill="var(--dark-2)"/>
      <path d="M1597,850 Q1520,1000 1320,1065 H1597 Z" fill="var(--dark-3)"/>
      <path d="M1597,955 Q1510,1030 1410,1065 H1597 Z" fill="var(--blue)"/>
    </g>

    <g class="academy-mark">
      <text class="academy-name" x="139" y="95">MARLOWE SUMMIT</text>
      <text class="academy-name" x="139" y="126">AVIATION ACADEMY</text>
    </g>

    <text class="title" x="800" y="222" text-anchor="middle">Certificate Of</text>
    <text class="title" x="800" y="340" text-anchor="middle">Completion</text>

    <g class="divider">
      <line class="dots" x1="398" y1="410" x2="762" y2="410"/>
      <line class="dots" x1="848" y1="410" x2="1212" y2="410"/>
      <rect x="783" y="393" width="34" height="34" transform="rotate(45 800 410)" fill="var(--dark-1)"/>
      <rect x="791" y="401" width="18" height="18" transform="rotate(45 800 410)" fill="var(--blue)"/>
    </g>

    <text class="label" x="349" y="540">CERTIFIES THAT</text>
    <text class="recipient" x="952" y="536" text-anchor="middle">Name Surname</text>
    <line class="rule" x1="645" y1="541" x2="1245" y2="541"/>
    <circle class="rule-end" cx="645" cy="541" r="4"/><circle class="rule-end" cx="1245" cy="541" r="4"/>

    <text class="label" x="800" y="623" text-anchor="middle">HAS SATISFACTORILY COMPLETED THE COURSE OF</text>
    <line class="rule" x1="427" y1="690" x2="1178" y2="690"/>
    <circle class="rule-end" cx="427" cy="690" r="4"/><circle class="rule-end" cx="1178" cy="690" r="4"/>

    <text class="label" x="472" y="765">ON</text>
    <line class="rule" x1="558" y1="765" x2="1140" y2="765"/>
    <circle class="rule-end" cx="558" cy="765" r="4"/><circle class="rule-end" cx="1140" cy="765" r="4"/>

    <g class="divider">
      <line class="dots" x1="398" y1="837" x2="762" y2="837"/>
      <line class="dots" x1="848" y1="837" x2="1212" y2="837"/>
      <rect x="783" y="820" width="34" height="34" transform="rotate(45 800 837)" fill="var(--dark-1)"/>
      <rect x="791" y="828" width="18" height="18" transform="rotate(45 800 837)" fill="var(--blue)"/>
    </g>

    <line class="rule" x1="510" y1="956" x2="1088" y2="956"/>
    <circle class="rule-end" cx="510" cy="956" r="4"/><circle class="rule-end" cx="1088" cy="956" r="4"/>
    <text class="signatory" x="799" y="991" text-anchor="middle">DANA WHITFIELD - HEAD OF OPERATIONS</text>
    <text class="signatory" x="799" y="1016" text-anchor="middle">MARLOWE SUMMIT AVIATION ACADEMY</text>

    <circle class="seal" cx="1376" cy="825" r="100" role="img" aria-label="Place for the gold seal of completion"/>
  </svg>
</main>
</body>
</html>
```